Email Signature Design

I need a Email Signature design that works on all devices and platforms. I have all the logo files and information for (4) people. It needs to be clean, fresh and reflect the simplicity of our logo. Two versions will be required, one for our main company and the same one for our sister company.

Industry/Entity Type

It Company

Requirements
Must have
• -Logo, Company Name, First and Last Name, Telephone #, Email, Website,
-Icon links for Face Book, Tumblr, etc that can be used or removed once we have those pages up and running
-(2) same or similar designs required, one for "Brova Properties" and one for "Brova Homes"
Nice to have
• QR Code with contact info and/or maybe

```html
<!DOCTYPE html>
<html lang="en">
<head>
<meta charset="utf-8">
<title>Brova Homes – Email Signature</title>
<link rel="stylesheet" href="https://fonts.googleapis.com/css2?family=Open+Sans:wght@400;600;700&display=swap">
<style>
  :root {
    --page-bg: #ffffff;
    --card-bg: #ffffff;
    --card-border: #dcdcdc;
    --header-light: #ffffff;
    --header-shade: #e6e6e6;
    --brand-ink: #1b1b1b;
    --name-blue: #1679c4;
    --label-blue: #3aa0e0;
    --body-text: #3a3a3a;
    --social-1: #3b5a98;
    --social-2: #0d77b5;
    --social-3: #2aa9e0;
    --social-4: #36465d;
    --social-5: #1fa1e0;
  }
  * { box-sizing: border-box; margin: 0; padding: 0; }
  html, body {
    width: 944px;
    height: 1200px;
    overflow: hidden;
    background: var(--page-bg);
    font-family: "Open Sans", Arial, sans-serif;
  }
  .signature-card {
    position: absolute;
    left: 72px;
    top: 48px;
    width: 795px;
    height: 1050px;
    background: var(--card-bg);
    border: 1px solid var(--card-border);
    border-radius: 8px;
    box-shadow: 0 3px 10px rgba(0,0,0,0.18);
    overflow: hidden;
  }
  .brand-header {
    height: 432px;
    background: radial-gradient(ellipse at 50% 40%, var(--header-light) 30%, var(--header-shade) 100%);
    display: flex;
    align-items: center;
    justify-content: center;
    gap: 22px;
  }
  .brand-mark {
    width: 44px;
    height: 44px;
    background: var(--brand-ink);
  }
  .brand-name {
    font-weight: 600;
    font-size: 52px;
    letter-spacing: 6px;
    color: var(--brand-ink);
  }
  .contact-block {
    padding: 38px 0 0 56px;
  }
  .company-name {
    font-weight: 700;
    font-size: 37px;
    color: var(--name-blue);
    line-height: 1.2;
    text-transform: uppercase;
  }
  .person-role {
    font-size: 32px;
    color: var(--body-text);
    margin-top: 10px;
  }
  .address {
    font-size: 31px;
    color: var(--body-text);
    margin-top: 36px;
  }
  .contact-line {
    font-size: 31px;
    color: var(--body-text);
    margin-top: 18px;
  }
  .contact-label {
    font-weight: 700;
    color: var(--label-blue);
  }
  .contact-label.is-dark { color: var(--body-text); }
  .web-link { color: var(--label-blue); text-decoration: none; }
  .social-links {
    display: flex;
    gap: 8px;
    margin-top: 46px;
  }
  .social-link {
    width: 58px;
    height: 58px;
    border-radius: 12px;
    display: block;
  }
  .social-link.s1 { background: var(--social-1); }
  .social-link.s2 { background: var(--social-2); }
  .social-link.s3 { background: var(--social-3); }
  .social-link.s4 { background: var(--social-4); }
  .social-link.s5 { background: var(--social-5); }
</style>
</head>
<body>
  <article class="signature-card">
    <header class="brand-header">
      <span class="brand-mark" aria-hidden="true"></span>
      <span class="brand-name">BROVA HOMES</span>
    </header>
    <section class="contact-block">
      <h1 class="company-name">Brova Homes</h1>
      <p class="person-role">Lorem Ipsum | Managing Director</p>
      <p class="address">1820 North Alder Avenue Marlow, SA 418209</p>
      <p class="contact-line"><span class="contact-label">Tel:</span> (318) 7420 61593</p>
      <p class="contact-line"><span class="contact-label">Email:</span> info@brovahomes.com</p>
      <p class="contact-line"><span class="contact-label">Fax:</span> (318) 7420 61593</p>
      <p class="contact-line"><span class="contact-label is-dark">Website:</span> <a class="web-link" href="#">www.brovahomes.com</a></p>
      <nav class="social-links" aria-label="Social profiles">
        <a class="social-link s1" href="#" aria-label="Social profile 1"></a>
        <a class="social-link s2" href="#" aria-label="Social profile 2"></a>
        <a class="social-link s3" href="#" aria-label="Social profile 3"></a>
        <a class="social-link s4" href="#" aria-label="Social profile 4"></a>
        <a class="social-link s5" href="#" aria-label="Social profile 5"></a>
      </nav>
    </section>
  </article>
</body>
</html>
```